Educational Software Company Seeking Event Postcard Design

We are looking for a postcard promoting an upcoming event. We would like to utilize the red, white and blue color scheme that you will see on the site at: http://plantstewards.campuswren.example/ksq. Gray can also be used. Please feel free to add some extra design elements. This postcard is targeting education operations professionals.

7th Annual Upper Granite Coast Grounds Stewards Summit

When: February 27th -28th

Where: Portsmouth, New Hampshire

Call to action - Register Today: linkbrief.example/GSS-Register

I have attached a word containing the text I'd like you to use and an example template. Some design elements will need to be added to the template

Red = bf1e2d
Blue = 0054a6

Target Market(s)

education operations professionals

Industry/Entity Type

Education

Requirements
Must have
• Grounds Stewards Summit logo, name of conference, date, location, blue, red, white and gray seen on website:

Red = bf1e2d
Blue = 0054a6

When: February 27th -28th

Please see attached word document called 2014_GSS_UGC Postcard for content.

```html
<!DOCTYPE html>
<html lang="en">
<head>
<meta charset="utf-8">
<title>Grounds Stewards Summit Postcard</title>
<link rel="stylesheet" href="https://fonts.googleapis.com/css2?family=Cormorant+SC:wght@600;700&family=Open+Sans:wdth,wght@75,300;75,400;75,700&display=swap">
<style>
  :root {
    --red: #bf1e2d;
    --blue: #0054a6;
    --blue-deep: #1f4e8c;
    --gray: #58595b;
    --gray-light: #a7a9ac;
    --paper: #ffffff;
    --frame: #c8c8c8;
  }
  * { margin: 0; padding: 0; box-sizing: border-box; }
  html, body {
    width: 1200px;
    height: 773px;
    overflow: hidden;
    background: var(--paper);
  }
  .postcard {
    position: relative;
    width: 1200px;
    height: 773px;
    background: var(--paper);
    border-right: 2px solid var(--frame);
    border-bottom: 2px solid var(--frame);
    border-left: 2px solid var(--frame);
    font-family: "Open Sans", sans-serif;
    font-stretch: 75%;
  }
  .event-mark {
    position: absolute;
    left: 52px;
    top: 86px;
    display: flex;
    align-items: center;
    gap: 16px;
  }
  .event-mark__dot {
    width: 92px;
    height: 92px;
    border-radius: 50%;
    background: var(--blue);
    flex: none;
  }
  .event-mark__name {
    font-weight: 700;
    font-size: 34px;
    line-height: 1.12;
    color: var(--blue);
    letter-spacing: 0.5px;
  }
  .event-info {
    position: absolute;
    left: 58px;
    top: 228px;
    width: 560px;
  }
  .event-info__when {
    font-family: "Cormorant SC", serif;
    font-weight: 700;
    font-size: 29px;
    line-height: 30px;
    color: var(--blue-deep);
    letter-spacing: 0.3px;
  }
  .event-info__intro {
    margin-top: 8px;
    font-weight: 300;
    font-size: 21.5px;
    line-height: 31px;
    color: var(--gray);
  }
  .topics {
    list-style: none;
    margin-top: 22px;
    font-weight: 300;
    font-size: 21.5px;
    line-height: 31.5px;
    color: var(--gray);
  }
  .topics li::before {
    content: "\2022";
    margin-right: 7px;
  }
  .register {
    margin-top: 24px;
    font-weight: 700;
    font-size: 30px;
    line-height: 34px;
    color: var(--red);
  }
  .divider {
    position: absolute;
    left: 642px;
    top: 40px;
    height: 676px;
    border-left: 2px dotted var(--gray-light);
  }
  .return-address {
    position: absolute;
    left: 668px;
    top: 46px;
    width: 120px;
    text-align: center;
  }
  .return-address__name {
    font-weight: 700;
    font-size: 25px;
    line-height: 26px;
    color: var(--blue);
  }
  .return-address__lines {
    margin-top: 10px;
    font-weight: 400;
    font-size: 10px;
    line-height: 13px;
    color: var(--gray);
  }
</style>
</head>
<body>
<main class="postcard">
  <header class="event-mark">
    <span class="event-mark__dot"></span>
    <p class="event-mark__name">Upper Granite Coast<br>Grounds Stewards Summit</p>
  </header>

  <section class="event-info">
    <h1 class="event-info__when">February 27th -28th<br>in Portsmouth, New Hampshire</h1>
    <p class="event-info__intro">This 2-day conference is packed with specialized networking, leadership and learning opportunities focused on facility and maintenance fundamentals for solving everyday challenges and achieving operational excellence. Some that will be discussed include:</p>
    <ul class="topics">
      <li>Facilities Management</li>
      <li>Energy Management</li>
      <li>Personnel Management</li>
      <li>School Safety</li>
      <li>Sustainability</li>
    </ul>
    <p class="register">Register Today: linkbrief.example/GSS-Register</p>
  </section>

  <div class="divider"></div>

  <address class="return-address">
    <p class="return-address__name">CampusWren</p>
    <p class="return-address__lines">4820 Lantern Ridge Drive<br>Suite #210<br>Millbrook, NC 27590</p>
  </address>
</main>
</body>
</html>
```